Online bill payment portal website design

Online Invoice Payment Website

The customer will click on the logos of the institution they want to pay and the payment will be made at the latest stage to write the customer number.

Invoice payment can be made online. Telephone, Television, Internet, Electricity, Water, Natural Gas, and all institutional payments.

Example website : https://www.selvopay.com/

Industry/Entity Type

Invoice

Logo Text

KolayBorcKapat.Net

Number of Pages Required

4 page

Font styles to use
Serif
Sans Serif

Colors
abd036
33a6d7
876aae
e667a6
ec1f27
f37122
85abd2
0555a3
00a990

Requirements
Must have
• Logos of payment institutions
• Credit Card Payment form
• Customer information form
• COntact page
• List of Institutions
• Accept privacy policies in all forms
Nice to have
• Good and new design :)
Should not have
• Same with selvopay.com ! i want new site

```html
<!DOCTYPE html>
<html lang="en">
<head>
<meta charset="utf-8">
<title>Billora – Select an invoice</title>
<link href="https://fonts.googleapis.com/css2?family=Questrial&display=swap" rel="stylesheet">
<style>
:root{
  --green-dark:#2f8a2c;
  --green:#4aa53e;
  --green-light:#85c16f;
  --green-text:#3a9a2d;
  --tick:#5cbf3a;
  --ink:#2b2b2b;
  --muted:#8a8a8a;
  --line:#dddddd;
  --tab:#e3e3e3;
  --tab-dark:#d8d8d8;
  --cell-due:#f0f0f0;
  --cell-border:#c9c9c9;
  --page:#ffffff;
  --report:#b7bedb;
}
*{box-sizing:border-box;margin:0;padding:0}
html,body{width:1200px;height:1071px;overflow:hidden;background:var(--page);
  font-family:"Questrial",sans-serif;color:var(--ink)}
.page{position:relative;width:1200px;height:1071px}
.topbar{position:absolute;left:0;top:0;width:1200px;height:100px;
  background:linear-gradient(180deg,var(--green) 0%,var(--green-dark) 100%)}
.brand{position:absolute;left:93px;top:34px;color:#fff;font-size:30px}
.topnav{position:absolute;right:93px;top:45px;display:flex;gap:34px;color:#fff;font-size:15px}
.topnav span{display:flex;align-items:center;gap:8px}
.catbar{position:absolute;left:0;top:100px;width:1200px;height:41px;background:#fff;
  box-shadow:0 6px 14px rgba(0,0,0,.04)}
.cats{position:absolute;left:91px;top:0;display:flex;height:41px;align-items:center;gap:0;font-size:14.5px;color:var(--muted)}
.cat{display:flex;align-items:center;gap:8px;margin-right:26px;height:41px;position:relative}
.cat.active{color:var(--ink)}
.cat.active::after{content:"";position:absolute;left:0;right:0;bottom:0;height:3px;background:var(--green)}
.search{position:absolute;right:89px;top:11px;display:flex;align-items:center;gap:10px;font-size:14.5px;color:var(--muted)}
.card{position:absolute;left:89px;top:192px;width:1022px;height:685px;background:#fff;
  box-shadow:0 2px 16px rgba(0,0,0,.06)}
.steps{display:flex;height:74px}
.step{width:249px;background:var(--tab);padding:22px 0 0 27px;color:#555}
.step:nth-child(2){background:var(--tab-dark)}
.step:last-child{flex:1}
.step.current{background:#fff;color:var(--green-text)}
.step small{display:block;font-size:12px;margin-bottom:4px}
.step b{font-weight:400;font-size:15.5px}
.inst-logo{position:absolute;left:83px;top:123px;width:141px;height:73px;background:#fff;
  box-shadow:0 2px 10px rgba(0,0,0,.1);display:flex;align-items:center;justify-content:center;
  font-size:25px;color:#e8552b}
.inst-name{position:absolute;left:249px;top:130px;font-size:25px}
.secure{position:absolute;left:249px;top:170px;font-size:15px;color:var(--green-text);display:flex;align-items:center;gap:6px}
.divider{position:absolute;left:83px;top:224px;width:958px;height:1px;background:var(--line)}
.lead{position:absolute;left:87px;top:258px;font-size:17px;color:#444}
.lead strong{font-weight:400;color:#111}
.months{position:absolute;left:83px;top:305px;display:grid;grid-template-columns:repeat(5,167px);
  grid-auto-rows:91px;column-gap:5px;row-gap:9px}
.month{position:relative;border:1px solid var(--cell-border);background:#fff;padding:9px 11px}
.month.due{background:var(--cell-due)}
.month h3{font-weight:400;font-size:22px;letter-spacing:.5px}
.month .tick{position:absolute;right:5px;top:5px}
.amounts{position:absolute;right:9px;bottom:8px;text-align:right;line-height:1.15}
.big{font-size:16px}
.small{font-size:12px}
.next{position:absolute;left:747px;top:624px;width:189px;height:36px;background:var(--green-light);
  border-radius:3px;box-shadow:0 0 0 3px #e6f1e2;color:#fff;font-size:14px;
  display:flex;align-items:center;justify-content:center;gap:8px}
.trademark{position:absolute;left:89px;top:976px;font-size:12px;color:#555}
.report{position:absolute;left:920px;top:962px;width:189px;height:36px;background:var(--report);
  border-radius:3px;box-shadow:0 0 0 3px #e4e7f2;color:#fff;font-size:14px;
  display:flex;align-items:center;justify-content:center;gap:8px}
.footline{position:absolute;left:89px;top:1009px;width:1022px;height:1px;background:var(--line)}
.footbrand{position:absolute;left:89px;top:1022px;font-size:22px;color:#666}
.footbrand span{font-size:12px;color:#aaa;margin-left:4px}
.footlinks{position:absolute;right:89px;top:1027px;display:flex;gap:25px;font-size:12.5px;color:#555}
</style>
</head>
<body>
<div class="page">
  <header class="topbar">
    <div class="brand">Billora</div>
    <nav class="topnav">
      <span><svg width="14" height="14" viewBox="0 0 14 14"><rect x="1" y="4" width="5" height="10" fill="#1f5e1c"/><rect x="7" y="1" width="6" height="13" fill="#1f5e1c"/></svg>Company</span>
      <span><svg width="16" height="16" viewBox="0 0 16 16"><circle cx="8" cy="8" r="8" fill="#1f5e1c"/><text x="8" y="12" font-size="11" text-anchor="middle" fill="#fff" font-family="sans-serif">?</text></svg>Help</span>
      <span><svg width="16" height="12" viewBox="0 0 16 12"><rect width="16" height="12" fill="#1f5e1c"/><path d="M0 0l8 6 8-6" stroke="#4aa53e" fill="none"/></svg>Contact</span>
    </nav>
  </header>

  <div class="catbar">
    <div class="cats">
      <span class="cat"><svg width="17" height="17" viewBox="0 0 17 17"><g fill="#999"><rect x="0" y="0" width="4" height="4"/><rect x="6" y="0" width="4" height="4"/><rect x="12" y="0" width="4" height="4"/><rect x="0" y="6" width="4" height="4"/><rect x="6" y="6" width="4" height="4"/><rect x="12" y="6" width="4" height="4"/><rect x="0" y="12" width="4" height="4"/><rect x="6" y="12" width="4" height="4"/><rect x="12" y="12" width="4" height="4"/></g></svg></span>
      <span class="cat"><svg width="16" height="16" viewBox="0 0 16 16"><circle cx="8" cy="8" r="7" fill="none" stroke="#999" stroke-width="2"/><path d="M8 1a7 7 0 0 1 0 14z" fill="#999"/></svg>Water</span>
      <span class="cat active"><svg width="14" height="16" viewBox="0 0 14 16"><rect x="3" y="0" width="2" height="5" fill="#3a9a2d"/><rect x="9" y="0" width="2" height="5" fill="#3a9a2d"/><path d="M1 5h12v4a6 6 0 0 1-12 0z" fill="#3a9a2d"/><rect x="6" y="13" width="2" height="3" fill="#3a9a2d"/></svg>Electricity</span>
      <span class="cat"><svg width="16" height="16" viewBox="0 0 16 16"><g fill="#999"><circle cx="8" cy="2" r="1.6"/><circle cx="8" cy="14" r="1.6"/><circle cx="2" cy="8" r="1.6"/><circle cx="14" cy="8" r="1.6"/><circle cx="4" cy="4" r="1.4"/><circle cx="12" cy="12" r="1.4"/><circle cx="12" cy="4" r="1.4"/><circle cx="4" cy="12" r="1.4"/></g></svg>Gaz</span>
      <span class="cat"><svg width="18" height="18" viewBox="0 0 18 18"><path d="M3 1l4 4-2 2c1 3 3 5 6 6l2-2 4 4-2 2C7 17 1 11 1 3z" fill="#999"/></svg>Phone</span>
      <span class="cat"><svg width="20" height="15" viewBox="0 0 20 15"><g fill="none" stroke="#999" stroke-width="2"><path d="M1 5a13 13 0 0 1 18 0"/><path d="M4 8.5a8.5 8.5 0 0 1 12 0"/></g><circle cx="10" cy="12.5" r="2" fill="#999"/></svg>Internet</span>
      <span class="cat"><svg width="20" height="17" viewBox="0 0 20 17"><rect x="1" y="1" width="18" height="12" fill="none" stroke="#999" stroke-width="2"/><rect x="6" y="14" width="8" height="2" fill="#999"/></svg>TV &amp; License</span>
    </div>
    <div class="search"><svg width="17" height="17" viewBox="0 0 17 17"><circle cx="7" cy="7" r="5.5" fill="none" stroke="#999" stroke-width="2"/><path d="M11 11l5 5" stroke="#999" stroke-width="2"/></svg>Search for institutions</div>
  </div>

  <main class="card">
    <div class="steps">
      <div class="step"><small>Step 1.</small><b>Select an institution</b></div>
      <div class="step"><small>Step 2.</small><b>Select your account</b></div>
      <div class="step current"><small>Step 3.</small><b>Select an invoice</b></div>
      <div class="step"><small>Step 4.</small><b>Payment</b></div>
    </div>

    <div class="inst-logo">Voltara</div>
    <div class="inst-name">Voltara</div>
    <div class="secure"><svg width="13" height="14" viewBox="0 0 13 14"><path d="M6.5 0L13 2v5c0 4-3 6-6.5 7C3 13 0 11 0 7V2z" fill="#5cbf3a"/><path d="M3.5 7l2 2 4-4" stroke="#fff" stroke-width="1.6" fill="none"/></svg>Secure Electricity bill&nbsp; payment</div>
    <div class="divider"></div>

    <p class="lead">Your Voltara monthly bills - <strong>Select a month to proceed payment</strong></p>

    <div class="months">
      <div class="month"><h3>January</h3><svg class="tick" width="17" height="17" viewBox="0 0 17 17"><circle cx="8.5" cy="8.5" r="8.5" fill="#5cbf3a"/><path d="M4.5 8.5l3 3 5-5" stroke="#fff" stroke-width="2" fill="none"/></svg><div class="amounts"><div class="big">Paid $59 USD</div><div class="small">Due $0 USD</div></div></div>
      <div class="month"><h3>February</h3><svg class="tick" width="17" height="17" viewBox="0 0 17 17"><circle cx="8.5" cy="8.5" r="8.5" fill="#5cbf3a"/><path d="M4.5 8.5l3 3 5-5" stroke="#fff" stroke-width="2" fill="none"/></svg><div class="amounts"><div class="big">Paid $59 USD</div><div class="small">Due $0 USD</div></div></div>
      <div class="month"><h3>March</h3><svg class="tick" width="17" height="17" viewBox="0 0 17 17"><circle cx="8.5" cy="8.5" r="8.5" fill="#5cbf3a"/><path d="M4.5 8.5l3 3 5-5" stroke="#fff" stroke-width="2" fill="none"/></svg><div class="amounts"><div class="big">Paid $59 USD</div><div class="small">Due $0 USD</div></div></div>
      <div class="month"><h3>April</h3><svg class="tick" width="17" height="17" viewBox="0 0 17 17"><circle cx="8.5" cy="8.5" r="8.5" fill="#5cbf3a"/><path d="M4.5 8.5l3 3 5-5" stroke="#fff" stroke-width="2" fill="none"/></svg><div class="amounts"><div class="big">Paid $59 USD</div><div class="small">Due $0 USD</div></div></div>
      <div class="month"><h3>May</h3><svg class="tick" width="17" height="17" viewBox="0 0 17 17"><circle cx="8.5" cy="8.5" r="8.5" fill="#5cbf3a"/><path d="M4.5 8.5l3 3 5-5" stroke="#fff" stroke-width="2" fill="none"/></svg><div class="amounts"><div class="big">Paid $59 USD</div><div class="small">Due $0 USD</div></div></div>
      <div class="month"><h3>June</h3><svg class="tick" width="17" height="17" viewBox="0 0 17 17"><circle cx="8.5" cy="8.5" r="8.5" fill="#5cbf3a"/><path d="M4.5 8.5l3 3 5-5" stroke="#fff" stroke-width="2" fill="none"/></svg><div class="amounts"><div class="big">Paid $59 USD</div><div class="small">Due $0 USD</div></div></div>
      <div class="month due"><h3>July</h3><div class="amounts"><div class="small">Paid $0 USD</div><div class="big">Due $59 USD</div></div></div>
      <div class="month due"><h3>August</h3><div class="amounts"><div class="small">Paid $0 USD</div><div class="big">Due $59 USD</div></div></div>
      <div class="month due"><h3>September</h3><div class="amounts"><div class="small">Paid $0 USD</div><div class="big">Due $59 USD</div></div></div>
      <div class="month due"><h3>October</h3><div class="amounts"><div class="small">Paid $0 USD</div><div class="big">Due $59 USD</div></div></div>
      <div class="month due"><h3>November</h3><div class="amounts"><div class="small">Paid $0 USD</div><div class="big">Due $59 USD</div></div></div>
      <div class="month due"><h3>December</h3><div class="amounts"><div class="small">Paid $0 USD</div><div class="big">Due $59 USD</div></div></div>
    </div>

    <div class="next"><svg width="17" height="14" viewBox="0 0 17 14"><path d="M0 7h15M9 1l6 6-6 6" stroke="#3d6b33" stroke-width="1.8" fill="none"/></svg>Next step</div>
  </main>

  <p class="trademark">All trademarks, names and logos are properties of their respective owners.</p>
  <div class="report"><svg width="19" height="19" viewBox="0 0 19 19"><circle cx="9.5" cy="9.5" r="9.5" fill="#d6dbee"/><rect x="8.5" y="8" width="2" height="6" fill="#b7bedb"/><circle cx="9.5" cy="5.5" r="1.2" fill="#b7bedb"/></svg>Report a problem</div>
  <div class="footline"></div>
  <div class="footbrand">Billora<span>© 2017</span></div>
  <nav class="footlinks"><span>About</span><span>Customers</span><span>Privacy</span><span>User Agreement</span><span>Legal</span><span>Feedback</span></nav>
</div>
</body>
</html>
```